Consultative Employee Benifits Firm Needs Business Card Design Project

We need a business card design for a new company based in Northern Virginia called "Tallow Ridge Advisors, LLC. We are both a wealth management advisory firm, as well as an employee benefits firm, which strives to provide superior creativity in employee benefits plan design and greater client and employee satisfaction. We are obsessed with service and follow up.

Our firm specializes in the areas of group health, life, dental, disability, voluntary benefits, Executive Benefits, HRA and HSA programs. We offer competitive employee benefit packages and pricing models for single or multi-state/multi location companies by maintaining preferred relationships with a large number of regional and national carriers.

Our firm also considers the many dimensions of your wealth through an integrated process we call wealth structuring — a comprehensive, dynamic approach to building, preserving, enjoying and transferring your wealth. And because we are often dealing with complex ownership structures and complicated, changing family dynamics, we bring the highest level of experience and creativity to managing your wealth. We work hard to help ensure that your legacy lasts by preparing your children for the financial challenges and opportunities that are headed their way.

Our final design should communicate an integrated approach to finanial safety and optimization
Updates

 Due to a few designers not accepting due to low budget, I have increased budget payout 19%. 

Project Deadline Extended
Reason: I have only heard from 12 designers. So, maybe I did not give the right amount of time to do the project. For the designers that have submitted their designs, thank you. I have seen three or four designs that I liked and might end up with one of them after it's all over, but I thought I would see between 20 - 25 before everything was over. Dean

Target Market(s)

Professionals; doctors, contractors, small to mid size business owners, ages 50 -65 with nert worth of 2MM

Industry/Entity Type

Financial

Requirements
Must have
• Tallow Ridge Advisors, LLC

Dean Harlow
President
17459 Marrowind Lane Street
Quenby Hollow, 20418

Office: 703 562-1094
Cell: 703 817-2650
Fax: 703 275-6831
Email: deanharlow@mailtrove.net
Should not have
• No pink or yellow colors.
No generic clipart (coins, dollar signs, money bags, graphs)

```html
<!DOCTYPE html>
<html lang="en">
<head>
<meta charset="utf-8">
<title>Tallow Ridge Advisors, LLC — Business Card</title>
<link rel="stylesheet" href="https://fonts.googleapis.com/css2?family=Quicksand:wght@400;500&family=Marcellus&display=swap">
<style>
  :root {
    --page-bg: #e6e6e6;
    --card-bg: #262627;
    --brand-blue: #2f56a6;
    --wave-dark: #1d2f6a;
    --wave-left: #22407f;
    --wave-right: #3b68b3;
    --text-light: #f2f4f8;
    --text-soft: #e3e8f2;
  }
  * { margin: 0; padding: 0; box-sizing: border-box; }
  html, body {
    width: 1200px;
    height: 970px;
    overflow: hidden;
    background: var(--page-bg);
  }
  .card {
    position: absolute;
    left: 80px;
    top: 182px;
    width: 1040px;
    height: 605px;
    background: var(--card-bg);
    overflow: hidden;
    font-family: "Quicksand", sans-serif;
    color: var(--text-light);
  }
  .card__wave {
    position: absolute;
    inset: 0;
    width: 100%;
    height: 100%;
  }
  .company-name {
    position: absolute;
    left: 40px;
    top: 30px;
    font-family: "Quicksand", sans-serif;
    font-weight: 500;
    font-size: 76px;
    line-height: 76px;
    letter-spacing: -1px;
    color: var(--brand-blue);
  }
  .person {
    position: absolute;
    right: 54px;
    top: 196px;
    text-align: right;
  }
  .person__name {
    font-family: "Marcellus", serif;
    font-size: 64px;
    line-height: 66px;
    color: #ffffff;
  }
  .person__title {
    font-family: "Quicksand", sans-serif;
    font-size: 34px;
    line-height: 40px;
    color: var(--text-soft);
  }
  .address {
    position: absolute;
    left: 48px;
    top: 330px;
    font-style: normal;
    font-size: 32px;
    line-height: 44px;
    color: var(--text-soft);
  }
  .contact {
    position: absolute;
    top: 487px;
    font-size: 31px;
    line-height: 40px;
    color: var(--text-light);
    list-style: none;
  }
  .contact--left { left: 48px; }
  .contact--right { left: 596px; }
</style>
</head>
<body>
  <section class="card" aria-label="Business card front">
    <svg class="card__wave" viewBox="0 0 736 428" preserveAspectRatio="none" aria-hidden="true">
      <defs>
        <linearGradient id="waveFill" x1="0" y1="0" x2="1" y2="0">
          <stop offset="0" stop-color="var(--wave-left)"/>
          <stop offset="1" stop-color="var(--wave-right)"/>
        </linearGradient>
      </defs>
      <path d="M0,334 C190,326 330,230 736,206 L736,428 L0,428 Z" fill="var(--wave-dark)"/>
      <path d="M0,342 C200,334 340,240 736,220 L736,428 L0,428 Z" fill="url(#waveFill)"/>
    </svg>

    <h1 class="company-name">Tallow Ridge<br>Advisors, LLC</h1>

    <div class="person">
      <p class="person__name">Dean Harlow</p>
      <p class="person__title">President</p>
    </div>

    <address class="address">
      17459 Marrowind Lane Street<br>
      Quenby Hollow, 20418
    </address>

    <ul class="contact contact--left">
      <li>Office: 703 562-1094</li>
      <li>Cell: 703 817-2650</li>
    </ul>
    <ul class="contact contact--right">
      <li>Fax: 703 275-6831</li>
      <li>Email: deanharlow@mailtrove.net</li>
    </ul>
  </section>
</body>
</html>
```